Veltrane Partners Website - developing a website for a new IIoT (Industrial Internet of Things) startup

Hi All-

Thought I'd re-write this bit...

Firstly, to everyone who has submitted designs, thank you.

Basically, we are looking for a simple/ elegant / modern website with clean lines and design. Because this is a startup, we don't have a great deal of content. Therefore, I'm relying on the site to give us an established / international feel (no images of London, London attractions, or the London skyline please!) We will have offices in London / LA and Tokyo by the end of this year.

Selecting great images is really important. As I say, abstract is fine (less literal.) Black and white is fine as well. We need to convey our expertise to new, international clients, so this is v.important.

http://www.pellucora41.it/ (favourite)
http://www.craftonvelmo.com/cases/

In terms of colour, I think white /grey/ black and maybe experiment with red for the word Veltrane and (possibly) Group. Please note** I need the following words / strap line written underneath the main logo: IIoT Strategy. Sensor Innovation. Machine Learning.

Whomever we chose to work with, this will be an ongoing partnership: we will continually need to add new content and update the site.

Thank you!

Tam.
Updates

**Please view updated brief description.

Target Market(s)

Mid-sized (£25M- £500M GBP) companies in the UK/ US and Asia. Facilities/ Construction/ Automotive/ Manufacturing / Engineering

Industry/Entity Type

Information Technology

Logo Text

Veltrane Partners -- IIoT Strategy. Sensor Innovation. Machine Learning (written underneath)

Coding

Coded - Design and coding required

Number of Pages Required

5+ page

Font styles to use
Sans Serif

Requirements
Must have
• An international, established, aspirational feel. Beautiful imagery. elegant infographics (nothing complex). CTA on homepage.
Should not have
• Anything cartoony / informal or naff corporate imagery.

```html
<!DOCTYPE html>
<html lang="en">
<head>
<meta charset="utf-8">
<title>Veltrane Partners</title>
<link href="https://fonts.googleapis.com/css2?family=Raleway:wght@300;400;500&family=Open+Sans:wght@300;400&display=swap" rel="stylesheet">
<style>
:root{
  --accent:#1cc3cf;
  --brand:#c8242b;
  --ink:#4a4a4a;
  --muted:#777;
  --soft:#999;
  --rule:#e4e4e4;
  --band:#efefef;
  --white:#fff;
  --hero-a:#6e7f93;
  --hero-b:#c9d3dc;
}
*{margin:0;padding:0;box-sizing:border-box}
html,body{width:779px;height:1200px;overflow:hidden;background:var(--white)}
body{position:relative;font-family:"Open Sans",sans-serif;color:var(--ink)}
.site-header{position:absolute;top:0;left:0;width:779px;height:43px;border-bottom:1px solid var(--rule);background:var(--white)}
.brand{position:absolute;left:65px;top:6px;font-family:"Raleway",sans-serif;font-size:15px;line-height:18px;font-weight:400;color:var(--brand)}
.brand-strapline{position:absolute;left:65px;top:26px;font-family:"Raleway",sans-serif;font-size:6.5px;line-height:8px;letter-spacing:.2px;color:var(--muted)}
.main-nav{position:absolute;right:65px;top:17px;display:flex;gap:24px;font-family:"Raleway",sans-serif;font-size:8px;color:var(--ink)}
.main-nav .active,.main-nav .contact{color:var(--accent)}
.nav-pointer{position:absolute;left:520px;top:42px;width:0;height:0;border-left:5px solid transparent;border-right:5px solid transparent;border-top:5px solid var(--white);z-index:2}
.hero{position:absolute;top:43px;left:0;width:769px;height:378px;overflow:hidden}
.hero-photo{position:absolute;inset:0;background:linear-gradient(110deg,var(--hero-a) 0%,var(--hero-b) 45%,#e2e7ec 60%,#5b6b80 100%)}
.hero-shade{position:absolute;inset:0;background:rgba(30,40,55,.28)}
.hero-copy{position:absolute;left:0;width:769px;top:132px;text-align:center;color:var(--white);font-family:"Raleway",sans-serif}
.hero-copy h1{font-size:29px;font-weight:400;letter-spacing:-1px}
.hero-copy h1 .lead{color:var(--accent);font-weight:300}
.hero-copy p{margin-top:9px;font-size:10.4px;line-height:13px}
.hero-cta{display:inline-block;margin-top:29px;padding:7px 10px;border:1px solid var(--accent);font-size:10px;color:var(--white)}
.hero-arrow{position:absolute;top:195px}
.hero-dots{position:absolute;left:361px;top:366px;display:flex;gap:3px}
.hero-dots span{width:16px;height:4px;border:1px solid var(--accent);border-radius:2px}
.hero-dots span:first-child{background:var(--accent)}
.intro{position:absolute;top:456px;left:72px;width:634px;text-align:center}
.section-title{position:relative;font-family:"Raleway",sans-serif;font-weight:400;font-size:21px;color:var(--ink)}
.section-title::before,.section-title::after{content:"";position:absolute;top:15px;width:210px;border-top:1px dashed #ccc}
.section-title::before{left:0}.section-title::after{right:0}
.intro p{margin-top:6px;font-size:11.3px;color:var(--muted)}
.services{position:absolute;top:526px;left:81px;display:flex;gap:25px}
.service{width:189px;text-align:left}
.service-icon{display:block;margin:0 auto;height:50px}
.service h2{margin-top:16px;text-align:center;font-family:"Raleway",sans-serif;font-weight:400;font-size:15px;color:var(--ink);padding-bottom:12px;border-bottom:1px solid var(--rule)}
.service p{margin-top:6px;font-size:8.6px;line-height:14.3px;font-weight:300;color:#666}
.read-more{display:block;text-align:right;margin-right:10px;margin-top:3px;font-size:8px;color:var(--muted)}
.events{position:absolute;top:810px;left:0;width:779px;height:390px;background:var(--band)}
.events-title{position:absolute;top:34px;left:65px;width:649px;text-align:center;font-family:"Raleway",sans-serif;font-size:17px;font-weight:400;color:var(--ink)}
.events-title strong{font-weight:500}
.events-title::before,.events-title::after{content:"";position:absolute;top:11px;width:232px;border-top:1px solid #ddd}
.events-title::before{left:0}.events-title::after{right:0}
.event-visual{position:absolute;left:86px;top:82px;width:269px;height:188px;border-radius:6px;background:#1d1d1d;padding:12px}
.event-visual div{width:100%;height:100%;background:linear-gradient(180deg,#3f86c4 0%,#a9cde6 40%,#d9cbb2 60%,#8a7560 100%)}
.event-pager{position:absolute;left:190px;top:336px;display:flex;gap:7px}
.event-pager span{width:10px;height:10px;border:1px solid #ccc}
.event-pager .on{border-color:var(--accent)}
.event-list{position:absolute;left:398px;top:81px;width:316px}
.event{height:51px}
.event h3{display:flex;align-items:center;gap:6px;font-family:"Open Sans",sans-serif;font-weight:300;font-size:10.4px;color:var(--ink)}
.event p{margin-left:16px;margin-top:2px;font-size:8px;line-height:11px;font-weight:300;color:var(--ink)}
.signup{position:absolute;left:398px;top:252px;padding:6px 6px;border:1px solid #ccc;background:var(--white);font-size:8.5px;color:var(--ink)}
</style>
</head>
<body>
<header class="site-header">
  <div class="brand">Veltrane Partners</div>
  <div class="brand-strapline">IIoT Strategy. Sensor Innovation. Machine Learning.</div>
  <nav class="main-nav">
    <span class="active">Home</span><span>About ▾</span><span>Events</span><span>Blog</span><span class="contact">Contact Us</span>
  </nav>
</header>
<div class="nav-pointer"></div>

<section class="hero">
  <div class="hero-photo" role="img" aria-label="Business partners shaking hands, seen from above"></div>
  <div class="hero-shade"></div>
  <svg class="hero-arrow" style="left:10px" width="14" height="30" viewBox="0 0 14 30"><path d="M13 1 1 15l12 14" fill="none" stroke="#fff" stroke-opacity=".6"/></svg>
  <svg class="hero-arrow" style="right:10px" width="14" height="30" viewBox="0 0 14 30"><path d="M1 1l12 14L1 29" fill="none" stroke="#fff" stroke-opacity=".7"/></svg>
  <div class="hero-copy">
    <h1><span class="lead">LET US</span> HELP YOU!</h1>
    <p>The core team at Veltrane Partners are a dedicated team of Innovators, PhDs and Computer Scientists and who help<br>mid-sized companies (£25M- £500M) realise the huge potential of deploying IIoT in their organisation.</p>
    <span class="hero-cta">READ MORE</span>
  </div>
  <div class="hero-dots"><span></span><span></span><span></span></div>
</section>

<section class="intro">
  <h2 class="section-title">Veltrane Partners</h2>
  <p>We provide expert advice to both new entrants and companies already familiar with IIoT</p>
</section>

<section class="services">
  <article class="service">
    <svg class="service-icon" width="50" height="50" viewBox="0 0 50 50" fill="#666"><circle cx="12" cy="10" r="6"/><circle cx="38" cy="10" r="6"/><circle cx="25" cy="16" r="8"/><path d="M1 30c0-8 5-11 11-11s7 2 7 2c-3 3-4 7-4 9z"/><path d="M49 30c0-8-5-11-11-11s-7 2-7 2c3 3 4 7 4 9z"/><path d="M9 48c0-12 6-20 16-20s16 8 16 20z"/></svg>
    <h2>Strategy</h2>
    <p>The Strategy team work with customers to navigate the complex world of IIoT and develop world-class strategies for maximising value. We know that connecting assets is not appropriate for every business: sometimes the challenges outweigh the rewards.</p>
    <span class="read-more">read more ⟶</span>
  </article>
  <article class="service">
    <svg class="service-icon" width="50" height="50" viewBox="0 0 50 50" fill="#666"><circle cx="16" cy="28" r="11"/><circle cx="37" cy="13" r="7"/><circle cx="39" cy="39" r="7"/><g stroke="#666" stroke-width="5"><path d="M16 12v32M0 28h32M5 17l22 22M27 17 5 39"/><path d="M37 3v20M27 13h20M30 6l14 14M44 6 30 20"/><path d="M39 29v20M29 39h20M32 32l14 14M46 32 32 46"/></g><circle cx="16" cy="28" r="4" fill="#fff"/><circle cx="37" cy="13" r="2.5" fill="#fff"/><circle cx="39" cy="39" r="2.5" fill="#fff"/></svg>
    <h2>Data &amp; AI</h2>
    <p>The Data &amp; AI team focus on getting the maximum value from our customer’s sensors. We are a small team of engineers and data scientists who know that the real value from IIoT comes from the quality of sensor data. We monitor and analyse this data and then deliver it to our customers via stunning dashboards.</p>
    <span class="read-more">read more ⟶</span>
  </article>
  <article class="service">
    <svg class="service-icon" width="50" height="50" viewBox="0 0 50 50"><circle cx="25" cy="25" r="19" fill="none" stroke="#666" stroke-width="8"/><g stroke="#fff" stroke-width="5"><path d="M11 11l8 8M39 11l-8 8M11 39l8-8M39 39l-8-8"/></g><circle cx="25" cy="25" r="23" fill="none" stroke="#666" stroke-width="2"/></svg>
    <h2>Sensors</h2>
    <p>The Sensor team are focused on innovation using Sensors and MEMS (Micro-Electromechanical Systems.) We view ourselves as the conduit between the vast array of complex sensors and their potential applications in the ‘real world.’</p>
    <span class="read-more">read more ⟶</span>
  </article>
</section>

<section class="events">
  <h2 class="events-title"><strong>UPCOMING</strong> EVENTS</h2>
  <div class="event-visual"><div role="img" aria-label="Display showing a wooden pier stretching out over a calm sea under a blue sky"></div></div>
  <div class="event-pager"><span></span><span></span><span class="on"></span><span></span></div>
  <div class="event-list">
    <div class="event">
      <h3><svg width="10" height="8" viewBox="0 0 10 8" fill="none" stroke="#444"><rect x="1.5" y=".5" width="7" height="5"/><path d="M0 7.5h10"/></svg>Title One</h3>
      <p>This can be replaced by 3 facts or important notes about the events upcoming in 2018.</p>
    </div>
    <div class="event">
      <h3><svg width="10" height="10" viewBox="0 0 10 10" fill="#444"><path d="M4 0l5 5-2 2-5-5z"/><path d="M4.5 5.5 1 9" stroke="#444" stroke-width="1.5"/></svg>Title Two</h3>
      <p>This can be replaced by 3 facts or important notes about the events upcoming in 2018.</p>
    </div>
    <div class="event">
      <h3><svg width="11" height="9" viewBox="0 0 11 9" fill="none" stroke="#444"><path d="M.5 0v8.5H11M2 7l3-3 2 2 3-4"/></svg>Title Three</h3>
      <p>This can be replaced by 3 facts or important notes about the events upcoming in 2018.</p>
    </div>
  </div>
  <span class="signup">Sign-up Here!</span>
</section>
</body>
</html>
```